Design a BOLD Ad Design for Fitness Club

We are fitness facility that is about to run our new "Bright Parent Reboot" program and we need a bold design created for an ad that will run on Instagram and Facebook.

The ad needs to be eye catching, easy to read and attractive so that someone stops scrolling and clicks to join.

The add needs to be sized to 1080 x 1080, include our logo and the text "Bright Parent Reboot" and "Starting September 23rd"

I have included an example photo, which is to be used as an example only of a design style that stands out to us, (colors, female photo style, etc)

I have also included our logo, which the yellow color can be changed for this design.

Thank you and we look forward to seeing your design.

```html
<!DOCTYPE html>
<html lang="en">
<head>
<meta charset="UTF-8">
<title>Bright Parent Reboot – Korevo</title>
<link rel="stylesheet" href="https://fonts.googleapis.com/css2?family=DM+Serif+Display&family=Poppins:wght@400;600;700;800&display=swap">
<style>
  :root {
    --ink: #0b0b0c;
    --gym-dark: #141416;
    --gym-mid: #2a2b2e;
    --brand-blue: #12b0ef;
    --white: #ffffff;
    --shirt-blue: #2fb5e6;
  }
  html, body {
    margin: 0;
    padding: 0;
    width: 1200px;
    height: 1200px;
    overflow: hidden;
    background: var(--ink);
  }
  .ad {
    position: relative;
    width: 1200px;
    height: 1200px;
    overflow: hidden;
    font-family: "Poppins", sans-serif;
    color: var(--white);
  }
  .gym-backdrop {
    position: absolute;
    inset: 0;
    background:
      linear-gradient(180deg, rgba(10,10,11,0.9) 0%, rgba(30,31,34,0.55) 45%, rgba(10,10,11,0.95) 100%),
      linear-gradient(90deg, var(--gym-dark) 0%, var(--gym-mid) 55%, var(--gym-dark) 100%);
  }
  .base-band {
    position: absolute;
    inset: 0;
    width: 1200px;
    height: 1200px;
  }
  .athlete-photo {
    position: absolute;
    left: 30px;
    top: 68px;
    width: 590px;
    height: 1070px;
    border-radius: 48% 48% 12% 12% / 30% 30% 6% 6%;
    background:
      radial-gradient(ellipse 45% 22% at 50% 40%, var(--shirt-blue) 0%, rgba(47,181,230,0.55) 60%, transparent 100%),
      linear-gradient(180deg, rgba(214,178,140,0.35) 0%, rgba(47,181,230,0.35) 30%, rgba(20,20,22,0.9) 60%, rgba(58,58,62,0.9) 100%);
  }
  .brand {
    position: absolute;
    right: 75px;
    top: 150px;
    width: 400px;
    text-align: center;
  }
  .brand-name {
    font-family: "Poppins", sans-serif;
    font-weight: 800;
    font-size: 104px;
    line-height: 1;
    letter-spacing: -2px;
    color: var(--white);
  }
  .brand-tagline {
    margin: 14px 0 0;
    font-size: 15px;
    font-weight: 700;
    letter-spacing: 2.5px;
    color: var(--brand-blue);
  }
  .headline {
    position: absolute;
    right: 55px;
    top: 335px;
    text-align: right;
    margin: 0;
    font-weight: 400;
  }
  .headline span { display: block; }
  .headline-top {
    font-family: "DM Serif Display", serif;
    font-size: 150px;
    line-height: 0.9;
    color: var(--white);
    margin-right: 50px;
  }
  .headline-mid {
    font-family: "DM Serif Display", serif;
    font-size: 160px;
    line-height: 0.75;
    color: var(--brand-blue);
    letter-spacing: -3px;
  }
  .headline-bottom {
    font-family: "Poppins", sans-serif;
    font-size: 82px;
    font-weight: 400;
    line-height: 1.15;
    letter-spacing: 2px;
    color: var(--white);
    margin-top: 14px;
  }
  .start-label {
    position: absolute;
    right: 75px;
    top: 718px;
    margin: 0;
    font-size: 56px;
    font-weight: 400;
    color: var(--white);
  }
  .date-pill {
    position: absolute;
    left: 480px;
    top: 801px;
    width: 675px;
    height: 84px;
    background: var(--brand-blue);
    border-radius: 0 42px 42px 0;
    display: flex;
    align-items: center;
    justify-content: flex-end;
    padding-right: 30px;
    box-sizing: border-box;
    font-size: 58px;
    font-weight: 700;
    color: var(--ink);
    letter-spacing: -0.5px;
  }
</style>
</head>
<body>
  <main class="ad">
    <div class="gym-backdrop" role="img" aria-label="Dimly lit gym interior with weight racks, medicine balls and benches in black and grey tones"></div>

    <svg class="base-band" viewBox="0 0 1200 1200" aria-hidden="true">
      <polygon points="0,1091 1200,1128 1200,1200 0,1200" fill="var(--brand-blue)"/>
    </svg>

    <div class="athlete-photo" role="img" aria-label="Smiling woman in a blue t-shirt and black leggings doing a lunge on a yoga mat, hands behind her head"></div>

    <header class="brand">
      <div class="brand-name">Korevo</div>
      <p class="brand-tagline">PERSONAL GROUP TRAINING</p>
    </header>

    <h1 class="headline">
      <span class="headline-top">Bright</span>
      <span class="headline-mid">Parent</span>
      <span class="headline-bottom">REBOOT</span>
    </h1>

    <p class="start-label">Starting</p>
    <div class="date-pill">September 23rd</div>
  </main>
</body>
</html>
```